A 24' X 36" SIGN TO ANNOUNCE "ORDER YOUR TURKEY EARLY"

MUST INCLUDE OUR LOGO(PROVIDED), black background, TEXT to include
all natural
farm raised
no hormones

The sign needs to be designed for vertical(portrait) viewing. The logo needs to be smaller and emphasis on TURKEY

Farm

```html
<!DOCTYPE html>
<html lang="en">
<head>
<meta charset="utf-8">
<title>Order Your Turkey Early – Hollenbeck Market</title>
<link rel="stylesheet" href="https://fonts.googleapis.com/css2?family=Bebas+Neue&family=Itim&display=swap">
<style>
  :root {
    --ink: #000000;
    --signal: #ffea00;
  }
  html, body {
    margin: 0;
    padding: 0;
    width: 800px;
    height: 1200px;
    overflow: hidden;
    background: var(--ink);
  }
  .sign {
    position: relative;
    width: 800px;
    height: 1200px;
    background: var(--ink);
    color: var(--signal);
    font-family: "Bebas Neue", "Oswald", sans-serif;
  }
  .sign-frame {
    position: absolute;
    inset: 0;
  }
  .headline-top,
  .headline-bottom {
    position: absolute;
    left: 0;
    width: 800px;
    margin: 0;
    text-align: center;
    font-weight: 400;
    line-height: 1;
    color: var(--signal);
  }
  .headline-top {
    top: 90px;
    font-size: 136px;
  }
  .turkey-band {
    position: absolute;
    left: 28px;
    top: 254px;
    width: 746px;
    height: 270px;
    background: var(--signal);
    display: flex;
    align-items: center;
    justify-content: center;
  }
  .turkey-word {
    margin: 0;
    font-size: 292px;
    font-weight: 400;
    line-height: 1;
    color: var(--ink);
    padding-top: 24px;
  }
  .headline-bottom {
    top: 563px;
    font-size: 146px;
  }
  .feature {
    position: absolute;
    display: flex;
    align-items: center;
    gap: 20px;
    font-family: "Itim", "Comic Sans MS", cursive;
    font-size: 62px;
    line-height: 1;
    color: var(--signal);
  }
  .feature-icon {
    width: 64px;
    height: 64px;
    flex: none;
  }
  .feature-natural { left: 156px; top: 752px; }
  .feature-farm { left: 332px; top: 854px; }
  .feature-hormones { left: 156px; top: 952px; }
  .market-name {
    position: absolute;
    left: 0;
    width: 800px;
    top: 1096px;
    text-align: center;
    font-size: 50px;
    line-height: 1;
    letter-spacing: 3px;
    color: var(--signal);
  }
</style>
</head>
<body>
<main class="sign">
  <svg class="sign-frame" width="800" height="1200" viewBox="0 0 800 1200" aria-hidden="true">
    <g fill="none" stroke="#ffea00" stroke-width="3">
      <polyline points="144,1118 28,1118 28,26 774,26 774,1118 656,1118"/>
    </g>
  </svg>

  <h1 class="headline-top">Order Your</h1>
  <div class="turkey-band">
    <h2 class="turkey-word">Turkey</h2>
  </div>
  <p class="headline-bottom">Early</p>

  <div class="feature feature-natural">
    <svg class="feature-icon" viewBox="0 0 64 64" aria-hidden="true">
      <circle cx="32" cy="32" r="32" fill="#ffea00"/>
      <path d="M33 14 C22 24 22 38 32 48 C42 38 42 24 33 14 Z" fill="#000"/>
      <path d="M32 48 L32 24" stroke="#ffea00" stroke-width="2"/>
      <path d="M24 34 C18 38 20 46 30 50" fill="none" stroke="#000" stroke-width="3"/>
    </svg>
    <span>All natural</span>
  </div>

  <div class="feature feature-farm">
    <svg class="feature-icon" viewBox="0 0 64 64" aria-hidden="true">
      <circle cx="32" cy="32" r="32" fill="#ffea00"/>
      <path d="M14 48 L14 28 L22 18 L42 18 L50 28 L50 48 Z" fill="#000"/>
      <rect x="28" y="22" width="8" height="6" fill="#ffea00"/>
      <rect x="22" y="32" width="20" height="16" fill="#ffea00"/>
      <rect x="25" y="35" width="14" height="13" fill="#000"/>
      <path d="M25 35 L39 48 M39 35 L25 48" stroke="#ffea00" stroke-width="2"/>
    </svg>
    <span>Farm raised</span>
  </div>

  <div class="feature feature-hormones">
    <svg class="feature-icon" viewBox="0 0 64 64" aria-hidden="true">
      <circle cx="32" cy="32" r="32" fill="#ffea00"/>
      <circle cx="32" cy="32" r="22" fill="none" stroke="#000" stroke-width="4"/>
      <g stroke="#000" stroke-width="3" fill="none" stroke-linecap="round">
        <rect x="26" y="21" width="10" height="22" transform="rotate(45 31 32)"/>
        <path d="M38 26 L44 20 M41 17 L47 23 M24 40 L19 45"/>
      </g>
      <path d="M17 17 L47 47" stroke="#000" stroke-width="4"/>
    </svg>
    <span>No hormones</span>
  </div>

  <p class="market-name">Hollenbeck Market</p>
</main>
</body>
</html>
```